New Modern High end Gin Design

We are looking for a new design for our current gin. The gin is named Moth Lantern Gin. We are looking for the bottle to be blue and the lettering to be gold. Please add the design on the bottle. the picture of the current bottle is in the uploaded files. we will not be using the same bottle. See photo attached with bottle type we would like to use. We would also like to make the rail cart imaged embossed

Font styles to use
Decorative

Colors
0054AA
0677BA
7BADD7
CADEEF
E8F1F8
0094D4
00A9DD
6FCCEA
C7EBF8
E9F6FB
FFC000
F8CF3A
FAE287
FDF2CF
FEFAEE

Requirements
Must have
• blue bottle
Nice to have
• ridges in the bottle

```html
<!DOCTYPE html>
<html lang="en">
<head>
<meta charset="utf-8">
<title>Moth Lantern Gin – Label</title>
<link href="https://fonts.googleapis.com/css2?family=Abril+Fatface&family=Cinzel:wght@700;900&display=swap" rel="stylesheet">
<style>
  :root {
    --page: #ffffff;
    --label-deep: #0054AA;
    --label-mid: #0677BA;
    --gold: #F8CF3A;
    --gold-soft: #FAE287;
    --gold-deep: #D9A93A;
    --gin-blue: #CADEEF;
  }
  html, body {
    margin: 0;
    width: 1200px;
    height: 1000px;
    overflow: hidden;
    background: var(--page);
  }
  .canvas {
    position: relative;
    width: 1200px;
    height: 1000px;
  }
  .label {
    position: absolute;
    left: 150px;
    top: 210px;
    width: 900px;
    height: 580px;
    background: linear-gradient(180deg, var(--label-mid) 0%, #1a6cb3 55%, var(--label-deep) 100%);
    overflow: hidden;
  }
  .label-lines {
    position: absolute;
    inset: 0;
  }
  .illustration {
    position: absolute;
    left: 640px;
    top: 24px;
    width: 230px;
    height: 226px;
    background: radial-gradient(ellipse at 50% 55%, rgba(248, 207, 58, 0.55), rgba(217, 169, 58, 0.25) 70%, rgba(217, 169, 58, 0) 100%);
    border-radius: 6px;
  }
  .product-name {
    position: absolute;
    margin: 0;
    font-family: "Abril Fatface", serif;
    font-weight: 400;
    color: var(--gold);
    line-height: 1;
    letter-spacing: 1px;
    white-space: nowrap;
  }
  .product-name--first {
    left: 56px;
    top: 52px;
    font-size: 150px;
  }
  .product-name--second {
    left: 168px;
    top: 244px;
    font-size: 118px;
  }
  .side-note {
    position: absolute;
    margin: 0;
    font-family: "Cinzel", serif;
    font-weight: 700;
    font-size: 22px;
    line-height: 1.05;
    color: var(--gold);
    letter-spacing: 1px;
  }
  .side-note--batch { left: 44px; top: 290px; }
  .side-note--place { right: 24px; top: 276px; text-align: right; }
  .spirit {
    position: absolute;
    left: 0;
    right: 0;
    top: 372px;
    margin: 0;
    text-align: center;
    font-family: "Cinzel", serif;
    font-weight: 900;
    font-size: 74px;
    line-height: 1;
    color: var(--gin-blue);
    letter-spacing: 2px;
  }
  .arc-text {
    font-family: "Cinzel", serif;
    font-weight: 700;
    fill: var(--gold);
  }
</style>
</head>
<body>
<main class="canvas">
  <section class="label" aria-label="Moth Lantern Gin bottle label">
    <svg class="label-lines" width="900" height="580" viewBox="0 0 900 580">
      <g stroke="var(--gold)" fill="none">
        <line x1="50" y1="30" x2="620" y2="30" stroke-width="4"/>
        <line x1="50" y1="42" x2="620" y2="42" stroke-width="1.5"/>
        <path d="M40 368 Q450 596 860 368" stroke-width="2"/>
        <path d="M40 430 Q450 658 860 430" stroke-width="2"/>
        <path d="M40 442 Q450 670 860 442" stroke-width="1.2"/>
        <path d="M70 372 Q230 436 340 430" stroke-width="1.5"/>
        <path d="M830 372 Q670 436 560 430" stroke-width="1.5"/>
      </g>
      <defs>
        <path id="arc-name" d="M40 410 Q450 638 860 410"/>
        <path id="arc-inner" d="M40 478 Q450 690 860 478"/>
      </defs>
      <text class="arc-text" font-size="32" letter-spacing="6">
        <textPath href="#arc-name" startOffset="50%" text-anchor="middle">IRON TRESTLE DISTILLERY</textPath>
      </text>
      <text class="arc-text" font-size="20" letter-spacing="1">
        <textPath href="#arc-inner" startOffset="6%">VOL 40%</textPath>
      </text>
      <text class="arc-text" font-size="20" letter-spacing="1">
        <textPath href="#arc-inner" startOffset="94%" text-anchor="end">750ML</textPath>
      </text>
    </svg>

    <div class="illustration" role="img" aria-label="Embossed gold illustration of workers pushing a rail cart"></div>

    <h1 class="product-name product-name--first">MOTH</h1>
    <p class="product-name product-name--second">LANTERN</p>

    <p class="side-note side-note--batch">SMALL<br>BATCH</p>
    <p class="side-note side-note--place">CEDAR<br>HOLLOW</p>

    <p class="spirit">GIN</p>
  </section>
</main>
</body>
</html>
```